Design logo and business card.

Design and construct logo and card for my business which is an over seeing company of other smaller businesses. The companies name is eleven5 venture alliance. Im open to any ideas but i am looking for a very cool contemporary design with a very prestige feel. The card can be either single or double sided, Thank you and i will look forward to your submissions.

Industry/Entity Type

Business

Requirements
Must have
• Company name, email, website, telephone, my name. Cool modern look with a prestige feel.

```html
<!DOCTYPE html>
<html lang="en">
<head>
<meta charset="UTF-8">
<title>eleven5 venture alliance — business card</title>
<link href="https://fonts.googleapis.com/css2?family=Questrial&display=swap" rel="stylesheet">
<style>
  :root {
    --page-bg: #ffffff;
    --card-black: #0b0b0b;
    --card-edge: #1a1a1a;
    --pattern-light: #2a2a2a;
    --pattern-dark: #070707;
    --silver: #d2d2d2;
    --accent-blue: #4a5fc4;
    --band-line: #3e4f9e;
    --text-white: #f2f2f2;
    --ghost-mark: #161616;
  }
  * { margin: 0; padding: 0; box-sizing: border-box; }
  html, body {
    width: 1200px;
    height: 900px;
    overflow: hidden;
    background: var(--page-bg);
    font-family: "Questrial", "Century Gothic", sans-serif;
  }
  .canvas {
    position: relative;
    width: 1200px;
    height: 900px;
  }
  .card {
    position: absolute;
    top: 290px;
    width: 540px;
    height: 320px;
    border-radius: 26px;
    background: var(--card-black);
    overflow: hidden;
    box-shadow: 0 18px 30px rgba(0, 0, 0, 0.18);
  }
  .card--front { left: 30px; }
  .card--back  { left: 630px; }

  /* Front */
  .damask-field {
    position: absolute;
    inset: 0;
    background: radial-gradient(ellipse at 40% 40%, var(--pattern-light) 0%, #181818 45%, var(--pattern-dark) 100%);
  }
  .front-wordmark {
    position: absolute;
    left: 84px;
    top: 78px;
    font-size: 92px;
    line-height: 1;
    color: var(--silver);
    letter-spacing: 1px;
  }
  .tagline-band {
    position: absolute;
    left: 0;
    right: 0;
    top: 226px;
    height: 34px;
    border-top: 1px solid var(--band-line);
    border-bottom: 1px solid var(--band-line);
  }
  .tagline {
    position: absolute;
    left: 26px;
    top: 3px;
    font-size: 21px;
    letter-spacing: 10.5px;
    color: var(--accent-blue);
    white-space: nowrap;
  }

  /* Back */
  .ghost-wordmark {
    position: absolute;
    left: 20px;
    top: 60px;
    font-size: 170px;
    line-height: 1;
    color: var(--ghost-mark);
    white-space: nowrap;
  }
  .contact-block {
    position: absolute;
    right: 130px;
    top: 82px;
    text-align: center;
  }
  .contact-name {
    font-size: 23px;
    color: var(--accent-blue);
  }
  .contact-phone {
    font-size: 19px;
    color: var(--text-white);
    margin-top: 2px;
  }
  .web-block {
    position: absolute;
    right: 120px;
    top: 208px;
    text-align: right;
    font-size: 19px;
    line-height: 1.3;
    color: var(--text-white);
    letter-spacing: 0.5px;
  }
</style>
</head>
<body>
<main class="canvas">
  <section class="card card--front">
    <div class="damask-field" role="img" aria-label="dark grey floral damask pattern"></div>
    <div class="front-wordmark">eleven5</div>
    <div class="tagline-band">
      <span class="tagline">venture alliance</span>
    </div>
  </section>

  <section class="card card--back">
    <div class="ghost-wordmark" aria-hidden="true">eleven5</div>
    <div class="contact-block">
      <p class="contact-name">Marco Vidal</p>
      <p class="contact-phone">+34 611 402 268</p>
    </div>
    <div class="web-block">
      <p class="contact-web">eleven-5.com</p>
      <p class="contact-email">hello@eleven-5.com</p>
    </div>
  </section>
</main>
</body>
</html>
```